Informative poster of frozen yogurt prices and sizes

Product is Frozen Yogurt. Need a menu poster A1/A0 size. Graphics showing 3 cup sizes (small $4, Medium $6 & Large $8). Extra 50Cent for each toppings (toppings includes stawberries, kiwi, nuts, candy etc.
for similar concept please refer to www.velmorasweets.com .
Design has to be clear and not too complicated

Target Market(s)

The poster is to be located at high traffic area. therefore it has to be very clear and precise and eye catching

Industry/Entity Type

Product

Requirements
Must have
• graphics of frozen yogurt cup, a variety of topping with prices. The prices has to be bold and clear. Easy to understand and not complicated.
Nice to have
• concept of value for money and healthy option dessert
Should not have
• too complicated background graphic

```html
<!DOCTYPE html>
<html lang="en">
<head>
<meta charset="utf-8">
<title>Frozen Yogurt Menu Poster</title>
<link rel="stylesheet" href="https://fonts.googleapis.com/css2?family=Open+Sans:ital,wght@0,400;0,700;0,800;1,400;1,700&family=Oswald:wght@700&display=swap">
<style>
  :root {
    --mount: #c4c4c4;
    --border: #ffffff;
    --cream: #fdf8f1;
    --halo: #ffffff;
    --yellow: #f5d970;
    --blue: #a9dde8;
    --pink: #f0a1b3;
    --ink: #6b6156;
    --text: #444444;
    --rule: #efe8de;
    --swirl: #f6b3ae;
    --cup: #c9e6f5;
    --berry: #e36a62;
    --kiwi: #8cc63f;
    --nut: #d49a5a;
    --candy-a: #f7b531;
    --candy-b: #d8245a;
    --candy-c: #36a9e1;
  }
  * { margin: 0; padding: 0; box-sizing: border-box; }
  html, body { width: 900px; height: 1200px; overflow: hidden; }
  body { background: var(--mount); font-family: "Open Sans", Arial, sans-serif; }
  .poster {
    position: absolute; left: 57px; top: 42px; width: 788px; height: 1116px;
    background: var(--border);
  }
  .poster-field {
    position: absolute; left: 9px; top: 12px; width: 770px; height: 1094px;
    background: var(--cream); overflow: hidden;
  }
  .halo {
    position: absolute; left: 128px; top: -188px; width: 540px; height: 540px;
    border-radius: 50%; background: var(--halo);
  }
  .headline { position: absolute; left: 0; top: 0; width: 770px; text-align: center; }
  .tagline {
    position: absolute; left: 0; width: 100%; top: 28px;
    font-size: 35px; font-weight: 400; color: var(--yellow); letter-spacing: 0.5px;
  }
  .title {
    position: absolute; left: 0; width: 100%;
    font-size: 104px; font-weight: 800; line-height: 1; letter-spacing: -1px;
  }
  .title-frozen { top: 66px; color: var(--blue); }
  .title-yogurt { top: 152px; color: var(--pink); }

  .size-card { position: absolute; text-align: center; }
  .cup-art {
    position: absolute; bottom: 0; border-radius: 60px 60px 4px 4px;
    background: linear-gradient(180deg, var(--swirl) 0%, var(--swirl) 50%, var(--cup) 52%, var(--cup) 100%);
  }
  .price {
    position: absolute; left: 0; width: 100%; top: 670px;
    font-family: "Oswald", "Arial Narrow", sans-serif; font-weight: 700;
    font-size: 48px; line-height: 1; color: var(--ink);
  }
  .size-name {
    position: absolute; left: 0; width: 100%; top: 714px;
    font-style: italic; font-size: 22px; color: var(--ink); letter-spacing: 1px;
  }
  .divider {
    position: absolute; left: 44px; top: 806px; width: 682px; height: 2px; background: var(--rule);
  }
  .toppings-label {
    position: absolute; left: 0; width: 100%; top: 848px; text-align: center;
    font-style: italic; font-size: 15px; color: var(--text); letter-spacing: 0.5px;
  }
  .topping { position: absolute; top: 896px; width: 160px; text-align: center; }
  .topping-art { display: block; margin: 0 auto; height: 58px; }
  .topping-name {
    display: block; margin-top: 18px; font-size: 17px; color: var(--text); letter-spacing: 1px;
  }
  .note {
    position: absolute; left: 0; width: 100%; top: 1058px; text-align: center;
    font-style: italic; font-size: 15px; color: var(--text); letter-spacing: 0.5px;
  }
  .note b { font-weight: 700; }
</style>
</head>
<body>
<div class="poster">
  <div class="poster-field">
    <div class="halo"></div>
    <div class="headline">
      <p class="tagline">VALUABLE &amp; HEALTHY</p>
      <h1 class="title title-frozen">FROZEN</h1>
      <h1 class="title title-yogurt">YOGURT</h1>
    </div>

    <div class="size-card" style="left:46px; top:0; width:173px; height:641px;">
      <div class="cup-art" role="img" aria-label="Illustration of a small frozen yogurt cup with pink swirl and toppings" style="left:0; width:173px; height:230px;"></div>
      <p class="price">$4</p>
      <p class="size-name">*Small</p>
    </div>
    <div class="size-card" style="left:289px; top:0; width:190px; height:641px;">
      <div class="cup-art" role="img" aria-label="Illustration of a medium frozen yogurt cup with pink swirl and toppings" style="left:0; width:190px; height:252px;"></div>
      <p class="price">$6</p>
      <p class="size-name">*Medium</p>
    </div>
    <div class="size-card" style="left:529px; top:0; width:208px; height:641px;">
      <div class="cup-art" role="img" aria-label="Illustration of a large frozen yogurt cup with pink swirl and toppings" style="left:0; width:208px; height:277px;"></div>
      <p class="price">$8</p>
      <p class="size-name">*Large</p>
    </div>

    <div class="divider"></div>
    <p class="toppings-label">Toppings:</p>

    <div class="topping" style="left:58px;">
      <span class="topping-art" role="img" aria-label="Strawberry slice illustration" style="width:108px; background:var(--berry); border-radius:0 0 54px 54px;"></span>
      <span class="topping-name">Strawberry</span>
    </div>
    <div class="topping" style="left:240px;">
      <span class="topping-art" role="img" aria-label="Kiwi slice illustration" style="width:106px; background:var(--kiwi); border-radius:0 0 53px 53px;"></span>
      <span class="topping-name">Kiwi</span>
    </div>
    <div class="topping" style="left:414px;">
      <span class="topping-art" role="img" aria-label="Nuts illustration" style="width:82px; background:var(--nut); border-radius:20px;"></span>
      <span class="topping-name">Nuts</span>
    </div>
    <div class="topping" style="left:588px;">
      <span class="topping-art" role="img" aria-label="Candy balls illustration" style="width:74px; border-radius:37px; background:linear-gradient(135deg, var(--candy-a), var(--candy-b) 55%, var(--candy-c));"></span>
      <span class="topping-name">Candy</span>
    </div>

    <p class="note">*Extra <b>50Cent</b> for each toppings</p>
  </div>
</div>
</body>
</html>
```